Lumen Pine Poster - Light Up the Lumen Pine With Your Visions for Peace

We would like owners of our Lumen Pine to be able to display an 11 by 17 poster next to it that explains what it is and what it does. Information about the Lumen Pine including a live video feed from one of them can be found at www.brightfoldstudio.example/lumenpine The Brightfold Studio Lumen Pine was designed to ask and hopefully answer the question: "Can a holiday decoration change the world?" Walter Hemsley, a guru of business management, is quoted to have said, "If you can't measure it, you can't change it." The lights on this tree are connected to the Internet and blink in response to people talking about peace on Chirpwave with the hashtag #peace. The lights will twinkle in a special way when anyone tweets with the combined hashtags of #peace #lumenpine. So whenever you are feeling a bit down about the state of the world, you can look at a lumen pine and be reminded that there are many people working to make the world a better place.

Target Market(s)

Individuals and organizations who purchase and display a lumen pine

Industry/Entity Type

Peacemaking, social justice, environmental justice, LGBTQQIA+, Inclusion/Diversity

Requirements
Must have
• "The Lights on This Lumen Pine Respond to the Number of People Tweeting About Peace. #Peace #Lumenpine. Share your visions of peace at brightfoldstudio.example/lumenpine to light up the world with peace." An eye popping design that clearly communicates what the Lumen Pine is and does. A tree with twinkling lights that is warm and inspiring
Nice to have
• The concept of world peace communicated overall
Should not have
• Nothing militaristic or violent

```html
<!DOCTYPE html>
<html lang="en">
<head>
<meta charset="utf-8">
<title>Lumen Pine Poster</title>
<link rel="stylesheet" href="https://fonts.googleapis.com/css2?family=Rubik:wght@700;800&family=Red+Hat+Display:wght@400;500;700&display=swap">
<style>
  :root {
    --ink-blue: #1b5aa3;
    --paper: #fafafa;
    --backdrop: #ecebe6;
    --pine-deep: #1f5a3c;
    --pine-light: #3f8a5a;
    --glow: #f6d77a;
  }
  * { margin: 0; padding: 0; box-sizing: border-box; }
  html, body {
    width: 1200px;
    height: 840px;
    overflow: hidden;
    background: var(--backdrop);
  }
  .canvas { position: relative; width: 1200px; height: 840px; }
  .poster {
    position: absolute;
    left: 314px;
    top: 20px;
    width: 571px;
    height: 800px;
    background: var(--paper);
    box-shadow: 0 2px 10px rgba(0,0,0,0.08);
  }
  .frame-outer { position: absolute; inset: 19px; border: 5px solid var(--ink-blue); }
  .frame-inner { position: absolute; inset: 28px; border: 1.5px solid var(--ink-blue); }
  .dove-emblem {
    position: absolute;
    left: 211px;
    top: 38px;
    width: 149px;
    height: 64px;
    background: var(--ink-blue);
    border-radius: 6px;
  }
  .headline {
    position: absolute;
    left: 40px;
    right: 40px;
    top: 112px;
    text-align: center;
    font-family: "Rubik", sans-serif;
    font-weight: 800;
    font-size: 35px;
    line-height: 38px;
    color: var(--ink-blue);
    letter-spacing: -0.2px;
  }
  .rule { position: absolute; height: 2px; background: var(--ink-blue); }
  .rule-top { left: 163px; width: 245px; top: 242px; }
  .rule-bottom { left: 201px; width: 168px; top: 518px; }
  .description {
    position: absolute;
    left: 50px;
    right: 50px;
    top: 256px;
    text-align: center;
    font-family: "Red Hat Display", sans-serif;
    font-weight: 500;
    font-size: 15.5px;
    line-height: 22.5px;
    color: var(--ink-blue);
  }
  .tree-lights {
    position: absolute;
    left: 62px;
    top: 532px;
    width: 120px;
    height: 116px;
    border-radius: 8px;
    background: radial-gradient(circle at 50% 45%, var(--glow) 0%, var(--pine-light) 35%, var(--pine-deep) 100%);
  }
  .goal {
    position: absolute;
    left: 196px;
    width: 320px;
    top: 534px;
    text-align: center;
    font-family: "Rubik", sans-serif;
    font-weight: 800;
    font-size: 24px;
    line-height: 28px;
    color: var(--ink-blue);
    letter-spacing: -0.2px;
  }
  .call-to-action {
    position: absolute;
    left: 56px;
    right: 56px;
    top: 660px;
    text-align: center;
    font-family: "Red Hat Display", sans-serif;
    font-size: 13.5px;
    line-height: 18px;
    color: var(--ink-blue);
  }
  .call-to-action .lead { font-weight: 700; }
  .call-to-action .share { font-weight: 500; margin-top: 4px; }
  .call-to-action .web-address { font-weight: 700; }
  .leaf-mark {
    position: absolute;
    left: 277px;
    top: 742px;
    width: 18px;
    height: 20px;
    border-radius: 50% 50% 50% 50% / 40% 40% 60% 60%;
    background: var(--ink-blue);
  }
</style>
</head>
<body>
<div class="canvas">
  <div class="poster">
    <div class="frame-outer"></div>
    <div class="frame-inner"></div>

    <div class="dove-emblem" role="img" aria-label="Two blue doves facing each other over a small sprouting leaf"></div>

    <h1 class="headline">Light up the Lumen<br>Pine with your own<br>visions of peace…</h1>

    <div class="rule rule-top"></div>

    <p class="description">
      The lights on this tree are connected to the<br>
      Internet and blink in response to people<br>
      talking about peace on Chirpwave with the<br>
      hashtag #peace. The lights will twinkle in a<br>
      special way when anyone tweets with the<br>
      combined hashtags of #peace<br>
      #lumenpine. So whenever you are feeling a<br>
      bit down about the state of the world, you<br>
      can look at a lumen pine and be reminded<br>
      that there are many people working to<br>
      make the world a better place.
    </p>

    <div class="rule rule-bottom"></div>

    <div class="tree-lights" role="img" aria-label="Warm glowing pine tree covered in twinkling lights"></div>

    <p class="goal">The hope is to have<br>200 of these trees<br>out in the world by<br>December, 2021</p>

    <div class="call-to-action">
      <p class="lead">The Lights on This Lumen Pine Respond to the Number of People Tweeting About Peace. #Peace #Lumenpine</p>
      <p class="share">Share your visions of peace at <span class="web-address">brightfoldstudio.example/lumenpine</span> to light up the world with peace.</p>
    </div>

    <div class="leaf-mark" role="img" aria-label="Small blue sprouting leaf ornament"></div>
  </div>
</div>
</body>
</html>
```